Flyer for an online formula one racing league

Hello.

I am looking for the perfect one page facebook/instagram style flyer for an online formula one racing league. The racing league is called 'VOLKA RACING LEAGUE'.

Information that MUST be on the new flyer is already on the old flyer I have uploaded here. In addition to including: The Volka racing league 'R' logo I have uploaded AND the text: 'Very popular, clean and competitive racing league, running for its 4th season. Why not join with a friend? Race times, Mondays, Tuesdays and Wednesdays each at 8pm UK TIME Message below for any questions. (Spacing of information is not important, however all the information in regards to the racing I have just mentioned MUST BE on the flyer, this includes info from old pic, logo and the other info I just mentioned).

It would be beneficial to have lots of dark blue on the flyer and the new flyer to be a lot different to the original flyer I uploaded, but this is not essential.

I apologise if I did not explain very well, any questions, please message me.

The best flyer should look the most attractive to someone that might be interested in joining an online formula one racing league.

I used this website before to create the perfect logo for my Sunday League team last year, and I was very impressed. I look forward to seeing your submissions.

Target Market(s)

No specific target, more something that may attract someone into joining a formula one online racing league

Industry/Entity Type

e sports/formula one

Colors
0054AA
0677BA
7BADD7
CADEEF
E8F1F8

Requirements
Must have
• Read product description please
Should not have
• Ignoring product description!

```html
<!DOCTYPE html>
<html lang="en">
<head>
<meta charset="utf-8">
<title>Volka Racing League – Season 4 Flyer</title>
<link rel="stylesheet" href="https://fonts.googleapis.com/css2?family=Audiowide&family=Saira+Condensed:wght@600&family=Montserrat:ital,wght@1,700;1,900&display=swap">
<style>
  :root {
    --page-bg: #0b1030;
    --navy-deep: #0a0f3d;
    --navy: #1b2a8a;
    --royal: #2f3fc9;
    --violet: #7a2fd0;
    --magenta: #e0308f;
    --pink-hot: #ff3fae;
    --glow-cyan: #3fd3ff;
    --yellow: #fff35a;
    --gold-shadow: #b8871e;
    --white: #ffffff;
    --frame: #ffffff;
  }
  * { margin: 0; padding: 0; box-sizing: border-box; }
  html, body {
    width: 1200px; height: 528px; overflow: hidden;
    background: var(--page-bg);
  }
  .canvas {
    position: relative; width: 1200px; height: 528px;
    display: flex; align-items: center; justify-content: center;
  }
  .flyer {
    position: relative; width: 1013px; height: 528px; overflow: hidden;
    background: var(--navy-deep);
  }
  .flyer-art {
    position: absolute; inset: 0;
    background:
      radial-gradient(ellipse 55% 45% at 62% 60%, rgba(255,63,174,0.75), transparent 70%),
      radial-gradient(ellipse 40% 40% at 82% 30%, rgba(122,47,208,0.7), transparent 70%),
      radial-gradient(ellipse 35% 30% at 70% 85%, rgba(63,211,255,0.35), transparent 70%),
      linear-gradient(160deg, var(--navy) 0%, var(--royal) 35%, var(--violet) 65%, var(--navy-deep) 100%);
  }
  .brand-mark {
    position: absolute; left: 28px; top: 56px;
    display: flex; align-items: center; gap: 10px;
  }
  .brand-mark .dot {
    width: 58px; height: 58px; border-radius: 50%;
    background: var(--navy-deep); border: 4px solid var(--pink-hot);
  }
  .brand-mark .name {
    font-family: "Audiowide", sans-serif; font-size: 26px; color: var(--white);
  }
  .title {
    position: absolute; left: 0; top: 0; width: 100%; height: 100%;
    transform: rotate(-7deg); transform-origin: 40% 40%;
  }
  .title-main, .title-sub {
    position: absolute; font-family: "Audiowide", sans-serif; line-height: 1;
    background: linear-gradient(180deg, var(--pink-hot) 0%, var(--magenta) 45%, var(--royal) 100%);
    -webkit-background-clip: text; background-clip: text; color: transparent;
    filter: drop-shadow(2px 3px 0 var(--white)) drop-shadow(0 0 6px rgba(255,255,255,0.4));
  }
  .title-main { left: 290px; top: 72px; font-size: 84px; letter-spacing: 2px; }
  .title-sub { left: 120px; top: 178px; font-size: 62px; letter-spacing: 1px; }
  .tagline {
    position: absolute; left: 58px; top: 330px; width: 900px;
    font-family: "Saira Condensed", sans-serif; font-weight: 600;
    font-size: 27px; letter-spacing: 3px; color: var(--white); text-transform: uppercase;
    transform: rotate(-9deg); transform-origin: left bottom; white-space: nowrap;
  }
  .season {
    position: absolute; left: 96px; top: 372px; text-align: center;
    font-family: "Montserrat", sans-serif; font-style: italic; font-weight: 900;
    font-size: 46px; line-height: 0.95; color: var(--yellow); text-transform: uppercase;
    text-shadow: 2px 3px 0 var(--gold-shadow), 0 0 3px var(--navy-deep);
    transform: rotate(-7deg);
  }
  .invite {
    position: absolute; left: 765px; top: 362px;
    font-family: "Montserrat", sans-serif; font-style: italic; font-weight: 700;
    font-size: 20px; line-height: 1.3; color: var(--white); text-transform: uppercase;
    text-shadow: 0 0 6px var(--violet);
  }
  .schedule {
    position: absolute; left: 708px; top: 420px;
    font-family: "Saira Condensed", sans-serif; font-weight: 600;
    letter-spacing: 1.5px; text-transform: uppercase; line-height: 1.55;
  }
  .schedule-heading {
    font-family: "Audiowide", sans-serif; font-size: 14px; color: var(--white);
    padding-left: 72px; letter-spacing: 2px;
  }
  .schedule-days, .schedule-time { font-size: 14.5px; color: var(--yellow); }
  .schedule-note { font-size: 14.5px; color: var(--white); }
</style>
</head>
<body>
<main class="canvas">
  <section class="flyer">
    <div class="flyer-art" role="img" aria-label="Pink and blue formula one car bursting out of a glowing screen onto a neon-lit track"></div>

    <div class="brand-mark">
      <span class="dot"></span>
      <span class="name">VOLKA</span>
    </div>

    <div class="title">
      <h1 class="title-main">VOLKA</h1>
      <p class="title-sub">RACING LEAGUE</p>
    </div>

    <p class="tagline">Very popular, clean and competitive racing league</p>

    <p class="season">Running for its<br>4th season</p>

    <p class="invite">Why not join<br>with a friend?</p>

    <div class="schedule">
      <p class="schedule-heading">RACE TIMES:</p>
      <p class="schedule-days">Mondays, Tuesdays and Wednesdays</p>
      <p class="schedule-time">Each at 8pm UK time</p>
      <p class="schedule-note">Message below for any questions.</p>
    </div>
  </section>
</main>
</body>
</html>
```